Business Card for New Greek Restaurant

Looking for a Business card for a new Greek Restaurant that's focus is on Take out and Delivery & catering.

Also to outline the contact information for the restaurant.
Does not require a name or title of a specific person (Just general business card)
Phone (519) 372-FETA (3382)
Email : info@bluefigkitchen.ca
Website : www.bluefigkitchen.ca

Facebook/Instagram/Twitter Icons to Follow us as well.

TAKEOUT * DELIVERY* CATERING

Target Market(s)

Woman Age 25-44

Industry/Entity Type

Greek Restaurant

Contact Information for Business Card

Card is to have the general contact information for the business as well as outline our Take Out and Catering Services. Existing Logo attached and to be incorporated into the design.

Font styles to use
Sans Serif

Colors

Designer to choose colors to be used in the design.

Requirements
Must have
• Restaurant Contact Information :
• Phone (519) 372-FETA (3382)
• Email : info@bluefigkitchen.ca
• Website : www.bluefigkitchen.ca
• Highlight Takeout, Catering, Delivery
• Business Address :
• Marlow Crossing
• 27 Hollister Rd., Unit 6
• Breslau ON
• N0B 2K4
Nice to have
• Modern Feel to promote TakeOut and Catering Services.
Should not have
• No Specific Title or Contact Person (Generic Business Card for Restaurant)

```html
<!DOCTYPE html>
<html lang="en">
<head>
<meta charset="utf-8">
<title>Blue Fig Kitchen – Business Card</title>
<link rel="stylesheet" href="https://fonts.googleapis.com/css2?family=Open+Sans:wght@400;600;700&display=swap">
<style>
  :root {
    --brand-blue: #29abe0;
    --brand-blue-deep: #1f9fd4;
    --card-white: #f2f2f2;
    --ink: #2b2b2b;
    --page: #e6e8ea;
    --on-blue: #ffffff;
  }
  * { box-sizing: border-box; margin: 0; padding: 0; }
  html, body { width: 1200px; height: 900px; overflow: hidden; }
  body {
    background: var(--page);
    font-family: "Open Sans", Arial, sans-serif;
    position: relative;
  }
  .card {
    position: absolute;
    left: 250px;
    width: 700px;
    height: 400px;
    overflow: hidden;
    box-shadow: 0 6px 18px rgba(0,0,0,0.18);
  }
  /* Back side */
  .card-back {
    top: 36px;
    background: linear-gradient(160deg, var(--brand-blue) 0%, var(--brand-blue-deep) 100%);
    color: var(--on-blue);
    text-align: center;
  }
  .card-back .brand-name {
    position: absolute;
    top: 120px; left: 0; right: 0;
    font-size: 46px;
    font-weight: 700;
    letter-spacing: 2px;
    color: var(--on-blue);
  }
  .follow {
    position: absolute;
    top: 286px; left: 0; right: 0;
    font-size: 15px;
    display: flex; align-items: center; justify-content: center; gap: 6px;
  }
  .follow::before, .follow::after {
    content: ""; width: 16px; height: 1px; background: var(--on-blue);
  }
  .social {
    position: absolute;
    top: 316px; left: 0; right: 0;
    display: flex; justify-content: center; gap: 22px;
  }
  .social span {
    width: 24px; height: 24px;
    border: 2px solid var(--on-blue);
    border-radius: 4px;
  }
  /* Front side */
  .card-front {
    top: 464px;
    background: var(--card-white);
  }
  .card-front .brand-name {
    position: absolute;
    top: 60px; left: 70px;
    font-size: 44px;
    font-weight: 700;
    letter-spacing: 2px;
    color: var(--brand-blue);
    white-space: nowrap;
  }
  .service-band {
    position: absolute;
    left: 0; top: 196px;
    width: 480px; height: 40px;
    background: var(--brand-blue);
    color: var(--on-blue);
    font-size: 17px;
    line-height: 40px;
    padding-left: 110px;
    word-spacing: 3px;
    white-space: nowrap;
  }
  .trident-art {
    position: absolute;
    left: 470px; top: 120px;
    width: 230px; height: 150px;
    background: var(--brand-blue);
    border-radius: 75px 0 0 75px;
  }
  .address {
    position: absolute;
    top: 268px; left: 150px;
    width: 230px;
    font-size: 16px;
    line-height: 1.4;
    color: var(--ink);
  }
  .divider {
    position: absolute;
    left: 385px; top: 296px;
    width: 1px; height: 72px;
    background: var(--ink);
  }
  .contact {
    position: absolute;
    top: 294px; left: 400px;
    font-size: 16px;
    line-height: 1.45;
    color: var(--ink);
    list-style: none;
    white-space: nowrap;
  }
  .contact li { display: flex; align-items: center; gap: 10px; }
  .contact svg { width: 14px; height: 14px; fill: none; stroke: var(--brand-blue); stroke-width: 2; }
</style>
</head>
<body>
  <section class="card card-back">
    <div class="brand-name">Blue Fig Kitchen</div>
    <div class="follow">Follow us</div>
    <div class="social"><span></span><span></span><span></span></div>
  </section>

  <section class="card card-front">
    <div class="brand-name">Blue Fig Kitchen</div>
    <div class="trident-art" role="img" aria-label="Large blue trident head illustration"></div>
    <div class="service-band">TAKEOUT | DELIVERY | CATERING</div>
    <p class="address">Marlow Crossing<br>27 Hollister Rd., Unit 6<br>Breslau ON N0B 2K4</p>
    <div class="divider"></div>
    <ul class="contact">
      <li><svg viewBox="0 0 16 16"><path d="M4 2l3 3-2 2c1 2 2 3 4 4l2-2 3 3-2 2C7 14 2 9 2 4z"/></svg>(519) 372-FETA (3382)</li>
      <li><svg viewBox="0 0 16 16"><rect x="2" y="4" width="12" height="9"/><path d="M2 4l6 5 6-5"/></svg>info@bluefigkitchen.ca</li>
      <li><svg viewBox="0 0 16 16"><circle cx="8" cy="8" r="6"/><path d="M2 8h12M8 2c3 3 3 9 0 12M8 2c-3 3-3 9 0 12"/></svg>www.bluefigkitchen.ca</li>
    </ul>
  </section>
</body>
</html>
```